Label for packages of Pure Raw Natural Honeycomb

This is a label that will be used to sell pure raw honeycomb on the internet and in farm gate sales
Label must contain my Logo (which is attached)
my website www.meadowglintfarm.ca
the weight 300 gr and the words Pure Raw Honeycomb
label design should fit onto a sticker 3" by 2" oval but If the size appears to small to get all that info on I am willing to look at a different size or shape

Target Market(s)

internet and in person farm gate customers

Industry/Entity Type

Agriculture

Font styles to use
Other font styles liked:
• the font should compliment my logo font

Colors
ffc214

Requirements
Must have
• Label must contain my Logo (attached) my website www.meadowglintfarm.ca
• the weight 300 gr and the words Pure Raw Honeycomb would like something in black and gold with a bit of an Elegant vintage feel
Nice to have
• vintage feel
• If the size appears to small to get all that info on I am willing to look at a different size or shape
Should not have
• no cartoons

```html
<!DOCTYPE html>
<html lang="en">
<head>
<meta charset="utf-8">
<title>Meadowglint Farm – Pure Raw Honeycomb Label</title>
<link href="https://fonts.googleapis.com/css2?family=Kaushan+Script&family=Roboto:wght@400&display=swap" rel="stylesheet">
<style>
  :root {
    --ink: #282624;
    --ink-deep: #1f1d1b;
    --gold-light: #f3df72;
    --gold: #e0b447;
    --gold-deep: #b8852e;
    --ornament: #c99d3e;
    --paper: #ffffff;
    --edge: #3a3a3a;
  }
  html, body {
    margin: 0;
    padding: 0;
    overflow: hidden;
    background: var(--paper);
  }
  .canvas {
    position: relative;
    width: 1200px;
    height: 1199px;
    box-sizing: border-box;
    border: 1px solid var(--edge);
    background: var(--paper);
  }
  .label-art {
    position: absolute;
    inset: 0;
    width: 100%;
    height: 100%;
  }
  .brand-name {
    font-family: "Kaushan Script", cursive;
    font-size: 50px;
    fill: var(--gold);
  }
  .product-name {
    font-family: "Kaushan Script", cursive;
    font-size: 92px;
    fill: var(--ink);
  }
  .net-weight {
    font-family: "Roboto", Arial, sans-serif;
    font-size: 40px;
    fill: var(--gold);
  }
  .net-weight .unit { font-size: 30px; }
</style>
</head>
<body>
<main class="canvas">
  <svg class="label-art" viewBox="0 0 1479 1478" xmlns="http://www.w3.org/2000/svg" aria-labelledby="label-title">
    <title id="label-title">Meadowglint Farm Pure Raw Honeycomb label, 300 gr</title>
    <defs>
      <linearGradient id="gold-frame" x1="0" y1="0" x2="1" y2="1">
        <stop offset="0" stop-color="var(--gold-light)"/>
        <stop offset="0.45" stop-color="var(--gold-deep)"/>
        <stop offset="0.7" stop-color="var(--gold-light)"/>
        <stop offset="1" stop-color="var(--gold-deep)"/>
      </linearGradient>
      <linearGradient id="gold-ribbon" x1="0" y1="0" x2="1" y2="0">
        <stop offset="0" stop-color="var(--gold-light)"/>
        <stop offset="0.35" stop-color="var(--gold)"/>
        <stop offset="0.65" stop-color="var(--gold-deep)"/>
        <stop offset="0.88" stop-color="var(--gold-light)"/>
        <stop offset="1" stop-color="var(--gold-deep)"/>
      </linearGradient>
      <path id="label-outline" d="M300 445 L525 440 A218 218 0 0 1 935 440 L1160 445 Q1230 450 1235 500 Q1290 520 1285 580 L1285 950 Q1290 1010 1240 1020 Q1200 1060 1150 1060 L1000 1060 Q850 1140 730 1145 Q610 1140 460 1060 L310 1060 Q240 1060 220 1020 Q170 1010 170 950 L170 580 Q170 520 225 500 Q240 450 300 445 Z"/>
      <path id="ribbon-line" d="M225 840 C 500 870, 800 790, 1250 770"/>
    </defs>

    <g class="label-body">
      <use href="#label-outline" fill="var(--ink)"/>
      <use href="#label-outline" fill="url(#gold-frame)" transform="translate(728 760) scale(0.955 0.935) translate(-728 -760)"/>
      <use href="#label-outline" fill="var(--ink)" transform="translate(728 760) scale(0.94 0.915) translate(-728 -760)"/>
      <use href="#label-outline" fill="url(#gold-frame)" transform="translate(728 760) scale(0.925 0.895) translate(-728 -760)"/>
      <use href="#label-outline" fill="var(--ink-deep)" transform="translate(728 760) scale(0.915 0.882) translate(-728 -760)"/>
    </g>

    <g class="ornaments" fill="var(--ornament)" opacity="0.55">
      <ellipse role="img" aria-label="Gold baroque flourish, upper left" cx="420" cy="610" rx="78" ry="62"/>
      <ellipse role="img" aria-label="Gold baroque flourish, upper right" cx="1040" cy="600" rx="78" ry="62"/>
      <ellipse role="img" aria-label="Gold baroque flourish, lower left" cx="320" cy="960" rx="65" ry="38"/>
      <ellipse role="img" aria-label="Gold baroque flourish, lower right" cx="1135" cy="950" rx="60" ry="40"/>
      <ellipse role="img" aria-label="Gold flourishes framing the weight oval" cx="730" cy="990" rx="185" ry="45"/>
    </g>

    <g class="brand-medallion">
      <circle cx="730" cy="515" r="212" fill="url(#gold-frame)"/>
      <circle cx="730" cy="515" r="203" fill="var(--ink)"/>
      <text class="brand-name" x="730" y="590" text-anchor="middle" textLength="300" lengthAdjust="spacingAndGlyphs">Meadowglint Farm</text>
    </g>

    <g class="ribbon">
      <path d="M190 685 C 400 760, 600 720, 800 680 C 1000 640, 1150 650, 1265 710 L1280 920 C 1150 860, 1000 850, 800 880 C 600 910, 400 930, 190 885 Z" fill="url(#gold-ribbon)"/>
      <path d="M205 705 C 400 775, 600 737, 800 697 C 1000 657, 1150 667, 1255 725" fill="none" stroke="var(--gold-deep)" stroke-width="3"/>
      <path d="M1265 905 C 1150 847, 1000 837, 800 865 C 600 895, 400 915, 205 870" fill="none" stroke="var(--gold-deep)" stroke-width="3"/>
      <text class="product-name">
        <textPath href="#ribbon-line" textLength="1020" lengthAdjust="spacingAndGlyphs">Pure Raw Honeycomb</textPath>
      </text>
    </g>

    <g class="weight-badge">
      <ellipse cx="733" cy="990" rx="92" ry="36" fill="var(--ink)" stroke="var(--gold)" stroke-width="2"/>
      <text class="net-weight" x="733" y="1004" text-anchor="middle">300 <tspan class="unit">gr</tspan></text>
    </g>
  </svg>
</main>
</body>
</html>
```